2016 Ledgerline Summit Postcard Design

The Ledgerline Summit. A Summit For Account Chasers...By Account Chasers.
The Ledgerline Summit was created to provide quality content at a reasonable price-point to allow organizations to send multiple attendees and encourage active participation. This event is intended for debt collection professionals who are:

Senior Level Executives
Front Line Collection Managers
Compliance Professionals
Trainers
While there are many great conferences within our industry to choose from, most collection conferences just scratch the surface when attempting to provide real world solutions. The Ledgerline Summit was created to provide debt collection professionals with a foundation of direction, insight, and actionable solutions that can be applied regardless of the size of an organization. Join us at the inaugural Ledgerline Summit as we assemble an expert team of operations, compliance, and training professionals that will deep dive into real world solutions for today’s real world debt collection issues. Here is what you can expect:

Solution driven sessions, not sponsor driven sessions
Substance from "In The Trenches" experts who live it, breathe it, work it...every day
Learn operational, compliance, and training strategies that have proven success
Understand how to efficiently and effectively manage YOUR resources
Apply state of the art technology solutions

Target Market(s)

Debt collection agencies and creditors

Industry/Entity Type

Financial Service

Font styles to use
Serif

Requirements
Must have
• link to website www.LLS2016.example and use of image provided LLSCover. Use same color scheme as the LLSCover image

```html
<!DOCTYPE html>
<html lang="en">
<head>
<meta charset="utf-8">
<title>2016 Ledgerline Summit Postcard</title>
<link href="https://fonts.googleapis.com/css2?family=Oswald:wght@200;300&family=Roboto+Condensed:ital,wght@0,300;0,400;1,400&family=Roboto:wght@400;700&display=swap" rel="stylesheet">
<style>
  :root {
    --panel: #1f2427;
    --teal: #3cc79c;
    --teal-deep: #2a8f77;
    --lime: #c8dc24;
    --olive: #69781f;
    --accent-yellow: #d8e41f;
    --text: #f2f2f2;
    --photo-light: #8d9294;
    --photo-dark: #232627;
  }
  html, body { margin: 0; padding: 0; overflow: hidden; background: #ffffff; }
  .postcard {
    position: relative; width: 1200px; height: 866px; overflow: hidden;
    display: flex; background: var(--panel);
  }

  /* Cover side */
  .cover { position: relative; width: 574px; height: 866px; overflow: hidden; }
  .cover-photo {
    position: absolute; inset: 0;
    background: linear-gradient(180deg, var(--photo-dark) 0%, var(--photo-light) 30%, #6f7476 48%, #3b3f41 62%, #545859 80%, #2a2d2e 100%);
  }
  .cover-overlay {
    position: absolute; left: 0; top: 0; width: 310px; height: 866px;
    background: linear-gradient(180deg, rgba(60,199,156,0.75) 0%, rgba(60,199,156,0.6) 40%, rgba(200,220,36,0.65) 70%, rgba(200,220,36,0.45) 100%);
    -webkit-mask-image: linear-gradient(90deg, #000 55%, transparent 100%);
    mask-image: linear-gradient(90deg, #000 55%, transparent 100%);
  }
  .brand-square {
    position: absolute; left: 200px; top: 588px; width: 58px; height: 58px; background: var(--teal);
  }
  .brand-rule {
    position: absolute; left: 280px; top: 602px; width: 1px; height: 150px; background: var(--text);
  }
  .brand-title {
    position: absolute; left: 298px; top: 600px; margin: 0;
    font-family: "Oswald", sans-serif; font-weight: 200; font-size: 40px;
    line-height: 52px; letter-spacing: 6px; color: var(--text);
  }
  .brand-title .year { color: var(--teal); font-weight: 300; }
  .cover-tagline {
    position: absolute; left: 298px; top: 757px; margin: 0;
    font-family: "Roboto", sans-serif; font-size: 11px; color: var(--text);
  }
  .cover-details {
    position: absolute; left: 298px; top: 788px; margin: 0;
    font-family: "Roboto", sans-serif; font-weight: 700; font-size: 13px; line-height: 17px; color: var(--text);
  }

  /* Info side */
  .info { position: relative; width: 626px; height: 866px; font-family: "Roboto Condensed", sans-serif; font-weight: 300; color: var(--text); }
  .info-band { position: absolute; left: 30px; width: 568px; }
  .info-band.top {
    top: 0; height: 44px;
    background: linear-gradient(90deg, var(--teal-deep) 0%, var(--teal-deep) 55%, var(--olive) 100%);
    opacity: 0.9;
  }
  .info-band.bottom {
    bottom: 0; height: 42px;
    background: linear-gradient(90deg, var(--teal-deep) 0%, var(--olive) 45%, var(--olive) 100%);
    opacity: 0.9;
  }
  .headline {
    position: absolute; left: 28px; width: 578px; top: 60px; margin: 0; text-align: center;
    font-style: italic; font-weight: 400; font-size: 22px; letter-spacing: -0.6px; color: var(--accent-yellow);
  }
  .copy {
    position: absolute; left: 28px; width: 578px; margin: 0;
    font-size: 17px; line-height: 28px; text-align: justify; text-align-last: center;
  }
  .intro { top: 106px; }
  .details { top: 359px; }
  .list { position: absolute; left: 28px; margin: 0; padding: 0; list-style: none; font-size: 17px; line-height: 28px; }
  .list li::before { content: "\2022"; margin-right: 6px; }
  .audience { top: 218px; }
  .expectations { top: 612px; }
  .site {
    position: absolute; left: 28px; width: 578px; top: 784px; margin: 0; text-align: center;
    font-weight: 400; font-size: 19px; color: var(--lime);
  }
</style>
</head>
<body>
<div class="postcard">
  <section class="cover">
    <div class="cover-photo" role="img" aria-label="Black and white photograph of a riverside city skyline with a tall steel arch under cloudy skies"></div>
    <div class="cover-overlay" role="img" aria-label="Translucent decorative geometric overlay in teal and lime tones"></div>
    <div class="brand-square"></div>
    <div class="brand-rule"></div>
    <h1 class="brand-title">LEDGERLINE<br>SUMMIT <span class="year">2016</span></h1>
    <p class="cover-tagline">A Summit for account chasers... by account chasers.</p>
    <p class="cover-details">SAINT LOUIS, MISSOURI<br>MARCH 21, 2016 - MARCH 23, 2016</p>
  </section>

  <section class="info">
    <div class="info-band top" role="img" aria-label="Decorative geometric band in teal and olive"></div>

    <h2 class="headline">A Summit For Account Chasers...By Account Chasers</h2>
    <p class="copy intro">The Ledgerline Summit was created to provide quality content at a reasonable price-point to allow organizations to send multiple attendees and encourage active participation. This event is intended for debt collection professionals who are:</p>
    <ul class="list audience">
      <li>Senior Level Executives</li>
      <li>Front Line Collection Managers</li>
      <li>Compliance Professionals</li>
      <li>Trainers</li>
    </ul>
    <p class="copy details">While there are many great conferences within our industry to choose from, most collection conferences just scratch the surface when attempting to provide real world solutions. The Ledgerline Summit was created to provide debt collection professionals with a foundation of direction, insight, and actionable solutions that can be applied regardless of the size of an organization. Join us at the inaugural Ledgerline Summit as we assemble an expert team of operations, compliance, and training professionals that will deep dive into real world solutions for today’s real world debt collection issues. Here is what you can expect:</p>
    <ul class="list expectations">
      <li>Solution driven sessions, not sponsor driven sessions</li>
      <li>Substance from "In The Trenches" experts who live it, breathe it, work it...every day</li>
      <li>Learn operational, compliance, and training strategies that have proven success</li>
      <li>Understand how to efficiently and effectively manage YOUR resources</li>
      <li>Apply state of the art technology solutions</li>
    </ul>
    <p class="site">www.LLS2016.example</p>

    <div class="info-band bottom" role="img" aria-label="Decorative geometric band in teal and olive"></div>
  </section>
</div>
</body>
</html>
```